Marigold's Lantern - Foundation PPT

Design a cohesive, emotionally resonant PowerPoint template that reflects the heart of Marigold’s Lantern Pregnancy & Family Support. This template will be used across fundraising, partnership, and storytelling presentations, and must balance professionalism with warmth, compassion, and human connection.

Background
Marigold’s Lantern Pregnancy & Family Support exists to support families navigating complicated pregnancies, prolonged hospital stays, and loss. The brand is rooted in empathy, quiet strength, and the concept of a “web” of care—an interconnected support system that surrounds families during difficult moments.

The template should feel deeply personal and mission-driven, not corporate.

Design Goals
Create a visually cohesive slide system that can be reused across multiple presentation types

Capture the emotional tone of the organization:
-Warm
-Gentle
-Hopeful
-Supportive
Ensure the design is clean, minimal, and easy to use for non-designers
Maintain a balance between storytelling and credibility

Key Design Requirements
-Brand Integration: Incorporate the Marigold’s Lantern logo (provided)
Align with soft, neutral color palette (e.g., cream, sage, blush, light sky tones)
-Use elegant, readable typography

Slide Templates to Include
-Cover Slide (emotion-forward, minimal text)
-Mission / Story Slide
-Program Overview Slide
-Impact / Metrics Slide
-Partnership / Sponsor Slide
-“Web of Support” Concept Slide (visual representation of interconnected care)
-Call to Action Slide
-Optional: Quote/Testimonial Slide

Visual Style
-Soft, calming, and approachable aesthetic
-Use of whitespace to avoid clutter
-Light use of icons or illustrations (if applicable)
-Avoid overly corporate or overly busy design elements

Usability
-Fully editable in PowerPoint
-Clear text hierarchy and placeholders
-Easy for internal team to update content without design support
-Tone & Emotional Direction

This is not a clinical or corporate presentation—it should feel human, heartfelt, and intentional.

website: https://www.marigoldslanterncare.org

```html
<!DOCTYPE html>
<html lang="en">
<head>
<meta charset="utf-8">
<title>Marigold's Lantern - Foundation Presentation Template</title>
<link href="https://fonts.googleapis.com/css2?family=Poppins:ital,wght@0,400;0,500;0,600;0,700;1,400&display=swap" rel="stylesheet">
<style>
:root{
  --bg:#e4e4e7;
  --paper:#ffffff;
  --mauve:#9a76ab;
  --mauve-deep:#8a6799;
  --teal:#7d9fa8;
  --sage:#7f8a7a;
  --blush:#c79c9f;
  --coral:#d59a8c;
  --ink:#4a4a4a;
  --muted:#a3a3a3;
  --rule:#d9cde0;
}
*{box-sizing:border-box;margin:0;padding:0}
html,body{width:1017px;height:1200px;overflow:hidden;background:var(--bg);font-family:'Poppins',sans-serif;color:var(--ink)}
.board{position:relative;width:1017px;height:1200px}
.slide{position:absolute;width:305px;height:172px;background:var(--paper);box-shadow:0 2px 6px rgba(0,0,0,.18);overflow:hidden}
.c1{left:33px}.c2{left:356px}.c3{left:679px}
.r1{top:40px}.r2{top:229px}.r3{top:418px}.r4{top:607px}.r5{top:797px}.r6{top:986px}
.abs{position:absolute}
.heading{position:absolute;left:12px;top:9px;font-size:10.5px;color:var(--mauve);font-weight:400;white-space:nowrap}
.heading b{font-weight:700}
.heading::after{content:"";position:absolute;left:0;top:17px;width:13px;height:2px;border-radius:1px;background:var(--teal)}
.brand-mini{position:absolute;right:10px;top:8px;display:flex;align-items:center;gap:2px;font-size:4.2px;font-weight:500;color:var(--mauve);white-space:nowrap}
.brand-mini i{display:block;width:6px;height:6px;border-radius:50%;background:var(--rule)}
.footer{position:absolute;left:8px;right:10px;top:156px;height:6px}
.footer i{position:absolute;left:0;top:0;width:5px;height:5px;border-radius:50%;background:var(--mauve);opacity:.7}
.footer span{position:absolute;left:10px;top:1px;font-size:1.8px;color:var(--muted);white-space:nowrap}
.footer::after{content:"";position:absolute;left:10px;right:8px;top:4px;height:.5px;background:var(--rule)}
.footer em{position:absolute;right:0;top:1px;font-style:normal;font-size:2.4px;color:var(--ink)}
.photo{position:absolute;border-radius:6px}
.t{position:absolute;font-size:6.2px;font-weight:500;color:var(--mauve);white-space:nowrap}
.p{position:absolute;font-size:3.1px;line-height:4px;color:var(--muted);text-align:justify}
.center{text-align:center}
.toc-row{position:absolute;height:8px}
.toc-row .lbl{position:absolute;left:0;top:0;font-size:4.4px;color:var(--mauve);white-space:nowrap}
.toc-row .lbl::before{content:"•";margin-right:2px}
.toc-row .ln{position:absolute;left:0;right:8px;top:5px;height:.5px;background:#cfcfcf}
.toc-row .num{position:absolute;right:0;top:1px;width:7px;height:7px;border-radius:50%;background:var(--teal);color:#fff;font-size:3.3px;line-height:7px;text-align:center;font-weight:600}
.bullet{position:absolute;left:168px;font-size:6px;color:var(--mauve);white-space:nowrap}
.bullet::before{content:"•";margin-right:3px}
.icon-tile{position:absolute;width:25px;height:25px;border-radius:4px;background:var(--teal);display:flex;align-items:center;justify-content:center}
.grid-cell{position:absolute;width:49px;height:48px;border-radius:4px;padding:6px 5px;color:#fff}
.grid-cell b{display:block;font-size:4.4px;margin-top:10px}
.grid-cell p{font-size:2.2px;line-height:3px;margin-top:2px;opacity:.9}
.grid-cell svg{position:absolute;left:5px;top:5px}
.feat-box{position:absolute;width:24px;height:24px;border:1px solid currentColor;border-radius:2px;display:flex;align-items:center;justify-content:center}
.feat-box::before{content:"";position:absolute;inset:2px;background:currentColor;border-radius:1px}
.feat-box svg{position:relative}
.feat-title{position:absolute;width:70px;font-size:4.3px;font-weight:700;text-align:center;color:#333}
.num-sq{position:absolute;left:148px;width:14px;height:14px;background:var(--mauve);color:#fff;font-size:9px;font-weight:700;line-height:14px;text-align:center}
.tl-item{position:absolute;width:60px;text-align:center}
.tl-item b{display:block;font-size:4.3px;color:var(--mauve);font-weight:600}
.tl-item span{display:block;font-size:3.4px;color:var(--muted);line-height:4.2px}
.team{position:absolute;top:56px;width:45px}
.team .band{height:19px}
.team .avatar{position:absolute;left:11px;top:7px;width:23px;height:23px;border-radius:50%;border:1.5px solid #fff}
.team b{position:absolute;top:37px;left:-6px;width:57px;text-align:center;font-size:5px;font-weight:600}
.team p{position:absolute;top:45px;left:-1px;width:47px;text-align:center;font-size:2.3px;line-height:3px;color:var(--muted)}
.contact{position:absolute;left:25px;display:flex;align-items:center;gap:4px;font-size:4.2px;line-height:5.4px;color:#fff}
.contact .bar{width:.6px;height:12px;background:#fff}
</style>
</head>
<body>
<div class="board">

<!-- 1 Cover -->
<section class="slide c1 r1">
  <div class="abs" style="left:22px;top:20px;font-size:8.5px;font-weight:500;color:var(--mauve);line-height:10px">Marigold’s Lantern<br><span style="font-size:4.4px;line-height:6px">Pregnancy &amp; Family Support</span></div>
  <div class="abs" style="left:19px;top:88px;font-size:15px;line-height:18px;font-weight:700;color:var(--mauve)">Company Title<br><span style="font-weight:400;color:var(--teal)">Goes Here</span></div>
  <div class="abs" style="left:19px;top:130px;font-size:7.5px;font-weight:600;color:var(--coral)">Presentation Template</div>
  <div class="abs" style="left:19px;top:141px;width:120px;font-size:4.2px;line-height:5px;color:var(--muted)">Lorem ipsum is simply dummy text of the printing and typesetting industry.</div>
  <div class="abs" role="img" aria-label="Flight of colourful butterflies rising across the slide" style="left:150px;top:0;width:155px;height:172px;background:radial-gradient(circle at 60% 35%,rgba(232,150,90,.45),transparent 55%),radial-gradient(circle at 35% 75%,rgba(214,96,70,.35),transparent 50%),radial-gradient(circle at 85% 20%,rgba(120,160,200,.3),transparent 45%),#fff"></div>
</section>

<!-- 2 Table of Contents -->
<section class="slide c2 r1">
  <div class="heading" style="color:var(--teal)">Table of <b style="color:var(--mauve)">Contents</b></div>
  <div class="brand-mini"><i></i>Marigold’s Lantern</div>
  <div class="toc-row" style="left:30px;width:112px;top:53px"><span class="lbl">Simple Text One</span><span class="ln"></span><span class="num">02</span></div>
  <div class="toc-row" style="left:30px;width:112px;top:71px"><span class="lbl">Simple Text Two</span><span class="ln"></span><span class="num">04</span></div>
  <div class="toc-row" style="left:30px;width:112px;top:89px"><span class="lbl">Simple Text Three</span><span class="ln"></span><span class="num">06</span></div>
  <div class="toc-row" style="left:30px;width:112px;top:106px"><span class="lbl">Simple Text Four</span><span class="ln"></span><span class="num">08</span></div>
  <div class="toc-row" style="left:30px;width:112px;top:124px"><span class="lbl">Simple Text Five</span><span class="ln"></span><span class="num">10</span></div>
  <div class="toc-row" style="left:163px;width:112px;top:53px"><span class="lbl">Simple Text One</span><span class="ln"></span><span class="num">02</span></div>
  <div class="toc-row" style="left:163px;width:112px;top:71px"><span class="lbl">Simple Text Two</span><span class="ln"></span><span class="num">04</span></div>
  <div class="toc-row" style="left:163px;width:112px;top:89px"><span class="lbl">Simple Text Three</span><span class="ln"></span><span class="num">06</span></div>
  <div class="toc-row" style="left:163px;width:112px;top:106px"><span class="lbl">Simple Text Four</span><span class="ln"></span><span class="num">08</span></div>
  <div class="toc-row" style="left:163px;width:112px;top:124px"><span class="lbl">Simple Text Five</span><span class="ln"></span><span class="num">10</span></div>
  <div class="footer"><i></i><span>Marigold’s Lantern Foundation</span><em>2</em></div>
</section>

<!-- 3 Image + three points -->
<section class="slide c3 r1">
  <div class="heading"><b>Heading</b> Goes Here</div>
  <div class="brand-mini"><i></i>Marigold’s Lantern</div>
  <div class="photo" role="img" aria-label="Butterfly resting on a purple daisy" style="left:31px;top:39px;width:100px;height:106px;background:radial-gradient(circle at 50% 50%,#c04f7a 0 14%,#8a5cc4 30%,#3d3a2f 80%)"></div>
  <div class="t" style="left:145px;top:40px">01. Text Added Here</div>
  <div class="p" style="left:145px;top:49px;width:131px">Lorem ipsum dolor sit amet, consectetuer adipiscing elit, sed diam nonummy nibh euismod tincidunt ut laoreet dolore magna aliquam erat volutpat. Ut wisi enim ad minim veniam, quis nostrud exerci tation.</div>
  <div class="t" style="left:145px;top:77px">02. Text Added Here</div>
  <div class="p" style="left:145px;top:86px;width:131px">Lorem ipsum dolor sit amet, consectetuer adipiscing elit, sed diam nonummy nibh euismod tincidunt ut laoreet dolore magna aliquam erat volutpat. Ut wisi enim ad minim veniam, quis nostrud exerci tation.</div>
  <div class="t" style="left:145px;top:114px">03. Text Added Here</div>
  <div class="p" style="left:145px;top:123px;width:131px">Lorem ipsum dolor sit amet, consectetuer adipiscing elit, sed diam nonummy nibh euismod tincidunt ut laoreet dolore magna aliquam erat volutpat. Ut wisi enim ad minim veniam, quis nostrud exerci tation.</div>
  <div class="footer"><i></i><span>Marigold’s Lantern Foundation</span><em>3</em></div>
</section>

<!-- 4 Photo + heading box -->
<section class="slide c1 r2">
  <div class="heading"><b>Heading</b> Goes Here</div>
  <div class="brand-mini"><i></i>Marigold’s Lantern</div>
  <div class="abs" role="img" aria-label="Team meeting around a bright office table" style="left:25px;top:41px;width:146px;height:62px;background:linear-gradient(120deg,#d9dde0,#b7a79a 45%,#e9ecee)"></div>
  <div class="abs" style="left:180px;top:48px;font-size:12px;line-height:13px;font-weight:600;color:var(--sage)">Heading<br><span style="font-size:10px;font-weight:400;color:var(--blush)">Text Goes Here</span></div>
  <div class="abs" style="left:123px;top:84px;width:160px;height:58px;background:var(--mauve);padding:5px 10px">
    <div style="font-size:7.5px;line-height:8.5px;font-weight:600;color:#fff">Text<br>Added Here</div>
    <div style="font-size:2.7px;line-height:3.6px;color:#fff;margin-top:3px;text-align:justify">Lorem ipsum dolor sit amet, cons ectetuer adipiscing elit, sed diam nonummy nibh euismod tincidunt ut laoreet dolore magna aliquam erat volutpat. Ut wisi enim ad minim veniam, quis nostrud exerci tation ullamcorper suscipit lobortis nisl ut aliquip ex ea commodo consequat.</div>
  </div>
  <div class="abs" style="left:28px;top:107px;font-size:6.8px;line-height:10px;font-weight:600;color:#8a8a7e"><span style="color:var(--mauve)">Adipiscing Elit</span><br>Sed Diam Nonummy<br>Nibh Euismod</div>
  <div class="footer"><i></i><span>Marigold’s Lantern Foundation</span><em>4</em></div>
</section>

<!-- 5 Section divider -->
<section class="slide c2 r2">
  <div class="abs" role="img" aria-label="Butterflies lifting from open hands against a pink and violet sky" style="left:0;top:19px;width:305px;height:133px;background:linear-gradient(100deg,#e7a6cf 0%,#d99be0 40%,#b79be4 70%,#c7b5ef 100%)"></div>
  <div class="abs" style="left:68px;top:44px;font-size:50px;line-height:54px;font-weight:700;color:#fff">01</div>
  <div class="abs" style="left:134px;top:60px;width:.7px;height:57px;background:#fff"></div>
  <div class="abs" style="left:143px;top:64px;font-size:14px;font-weight:700;color:#fff">Part One.</div>
  <div class="abs" style="left:143px;top:85px;width:110px;font-size:5px;line-height:6.5px;color:#fff">Lorem ipsumectetuer adipiscing elit sed diam nonummy nibh euismod tincidunt</div>
</section>

<!-- 6 Text + bullets -->
<section class="slide c3 r2">
  <div class="heading"><b>Heading</b> Goes Here</div>
  <div class="brand-mini"><i></i>Marigold’s Lantern</div>
  <div class="t" style="left:25px;top:40px;font-size:5.8px">01. Text Added Here</div>
  <div class="p" style="left:25px;top:48px;width:126px">Lorem ipsum dolor sit amet, cons ectetuer adipiscing elit, sed diam nonummy nibh euismod tincidunt ut laoreet dolore magna aliquam erat volutpat. Ut wisi enim ad minim veniam, quis nostrud exerci tation ullamcorper suscipit lobortis nisl ut aliquip ex ea commodo consequat.<br><br>Lorem ipsum dolor sit amet, consectetuer adipiscing elit, sed diam nonummy nibh euismod tincidunt ut laoreet dolore magna aliquam erat volutpat. Ut wisi enim ad minim veniam, quis nostrud exerci tation.</div>
  <div class="t" style="left:25px;top:102px;font-size:5.8px">02. Text Added Here</div>
  <div class="p" style="left:25px;top:110px;width:126px">Lorem ipsum dolor sit amet, consectetuer adipiscing elit, sed diam nonummy nibh euismod tincidunt ut laoreet dolore magna aliquam erat volutpat. Ut wisi enim ad minim veniam, quis nostrud exerci tation.<br><br>Lorem ipsum dolor sit amet, consectetuer adipiscing elit, sed diam nonummy nibh.</div>
  <div class="bullet" style="top:51px">Fits Your Business Or Products</div>
  <div class="bullet" style="top:68px">Is Easy To Spell And Remember</div>
  <div class="bullet" style="top:85px">Fits Your Business Or Products</div>
  <div class="bullet" style="top:102px">Is Easy To Spell And Remember</div>
  <div class="bullet" style="top:118px">Fits Your Business Or Products</div>
  <div class="bullet" style="top:135px">Is Easy To Spell And Remember</div>
  <div class="footer"><i></i><span>Marigold’s Lantern Foundation</span><em>6</em></div>
</section>

<!-- 7 Mission / Vision -->
<section class="slide c1 r3">
  <div class="heading"><b>Heading</b> Goes Here</div>
  <div class="brand-mini"><i></i>Marigold’s Lantern</div>
  <div class="abs" style="left:18px;top:35px;width:125px;font-size:4.6px;line-height:6px;font-style:italic;color:#777">Lorem ipsum dolor sit amet, cons ectetuer adipiscing elit, sed diam nonummy nibh euismod tincidunt.Lorem ipsum dolor sit amet.</div>
  <div class="photo" role="img" aria-label="Parents folding baby clothes together at home" style="left:21px;top:66px;width:132px;height:71px;background:linear-gradient(110deg,#7e8f5e,#c9c2b0 50%,#9aa3a0)"></div>
  <div class="icon-tile" style="left:166px;top:59px"><svg width="13" height="13" viewBox="0 0 24 24" fill="none" stroke="#fff" stroke-width="1.6"><path d="M4 20l6-6M9 9l6 6M12 4l8 8-4 1-5-5z"/></svg></div>
  <div class="t" style="left:198px;top:59px;font-size:7px;font-weight:600">Our Mission</div>
  <div class="abs" style="left:198px;top:69px;width:85px;font-size:3.6px;line-height:4.6px;font-style:italic;color:var(--muted)">Lorem ipsum dolor sit amet, cons ectetuer adipiscing elit, sed diam nonummy nibh euismod tincidunt.</div>
  <div class="icon-tile" style="left:166px;top:107px"><svg width="13" height="13" viewBox="0 0 24 24" fill="none" stroke="#fff" stroke-width="1.6"><path d="M4 20L20 4M4 4l16 16M7 4h-3v3M17 20h3v-3"/></svg></div>
  <div class="t" style="left:198px;top:107px;font-size:7px;font-weight:600">Our Vision</div>
  <div class="abs" style="left:198px;top:117px;width:85px;font-size:3.6px;line-height:4.6px;font-style:italic;color:var(--muted)">Lorem ipsum dolor sit amet, cons ectetuer adipiscing elit, sed diam nonummy nibh euismod tincidunt.</div>
  <div class="footer"><i></i><span>Marigold’s Lantern Foundation</span><em>7</em></div>
</section>

<!-- 8 Process -->
<section class="slide c2 r3">
  <div class="heading"><b>Heading</b> Goes Here</div>
  <div class="brand-mini"><i></i>Marigold’s Lantern</div>
  <div class="abs" role="img" aria-label="Faint world map backdrop" style="left:45px;top:28px;width:220px;height:100px;border-radius:50%;background:radial-gradient(ellipse,#f0f0f0 40%,transparent 72%)"></div>
  <svg class="abs" style="left:0;top:0" width="305" height="172" viewBox="0 0 305 172" fill="none" stroke="#7d9fa8" stroke-width="1.6">
    <path d="M98 40H60a3 3 0 0 0-3 3v84a3 3 0 0 0 3 3h40l12-16"/>
    <path d="M110 58l-12 16v45"/>
    <path d="M125 130V56l12-16h42a3 3 0 0 1 3 3v33"/>
    <path d="M166 130h13a3 3 0 0 0 3-3v-10"/>
    <path d="M203 40h44a3 3 0 0 1 3 3v84a3 3 0 0 1-3 3h-37a3 3 0 0 1-3-3v-10"/>
    <circle cx="112" cy="58" r="2.2" fill="#7d9fa8"/><circle cx="182" cy="76" r="2.2" fill="#7d9fa8"/><circle cx="207" cy="117" r="2.2" fill="#7d9fa8"/>
  </svg>
  <svg class="abs" style="left:81px;top:52px" width="9" height="10" viewBox="0 0 24 24" fill="none" stroke="#7d9fa8" stroke-width="2"><path d="M12 2a7 7 0 0 0-4 13v3h8v-3a7 7 0 0 0-4-13zM9 22h6"/></svg>
  <svg class="abs" style="left:150px;top:53px" width="11" height="9" viewBox="0 0 24 20" fill="none" stroke="#7d9fa8" stroke-width="2"><rect x="2" y="2" width="20" height="16"/><path d="M2 2l10 9 10-9"/></svg>
  <svg class="abs" style="left:221px;top:53px" width="10" height="9" viewBox="0 0 24 22" fill="none" stroke="#7d9fa8" stroke-width="2"><path d="M2 2v18h20M6 15l5-6 4 4 6-8"/></svg>
  <div class="abs center" style="left:60px;top:66px;width:50px;font-size:4.6px;font-weight:600;color:var(--mauve)">IDEA</div>
  <div class="p center" style="left:64px;top:73px;width:42px;font-size:2.3px;line-height:3px">Lorem ipsum dolor sit amet, consectetuer adipiscing elit, sed diam nonummy nibh euismod tincidunt ut laoreet dolore magna aliquam erat volutpat. Ut wisi enim ad minim veniam, quis nostrud exerci tation ullamcorper suscipit lobortis nisl ut aliquip ex ea commodo.</div>
  <div class="abs center" style="left:128px;top:66px;width:54px;font-size:4.6px;font-weight:600;color:var(--mauve)">PROMOTION</div>
  <div class="p center" style="left:134px;top:73px;width:42px;font-size:2.3px;line-height:3px">Lorem ipsum dolor sit amet, consectetuer adipiscing elit, sed diam nonummy nibh euismod tincidunt ut laoreet dolore magna aliquam erat volutpat. Ut wisi enim ad minim veniam, quis nostrud exerci tation ullamcorper suscipit lobortis nisl ut aliquip ex ea commodo.</div>
  <div class="abs center" style="left:201px;top:66px;width:50px;font-size:4.6px;font-weight:600;color:var(--mauve)">GROWTH</div>
  <div class="p center" style="left:205px;top:73px;width:42px;font-size:2.3px;line-height:3px">Lorem ipsum dolor sit amet, consectetuer adipiscing elit, sed diam nonummy nibh euismod tincidunt ut laoreet dolore magna aliquam erat volutpat. Ut wisi enim ad minim veniam, quis nostrud exerci tation ullamcorper suscipit lobortis nisl ut aliquip ex ea commodo.</div>
  <div class="p center" style="left:38px;top:134px;width:230px;font-size:3.1px">Lorem ipsum dolor sit amet, consectetuer adipiscing elit, sed diam nonummy nibh euismod tincidunt ut laoreet dolore magna aliquam erat volutpat. Ut wisi enim ad minim veniam, quis nostrud exerci tation ullamcorper suscipit lobortis nisl ut aliquip ex ea commodo consequat. Duis autem vel eum iriure dolor in hendrerit.</div>
  <div class="footer"><i></i><span>Marigold’s Lantern Foundation</span><em>8</em></div>
</section>

<!-- 9 Two columns -->
<section class="slide c3 r3">
  <div class="heading"><b>Heading</b> Goes Here</div>
  <div class="brand-mini"><i></i>Marigold’s Lantern</div>
  <div class="t" style="left:25px;top:39px;font-size:8px">01. Text Added Here</div>
  <div class="p" style="left:25px;top:51px;width:121px">Lorem ipsum dolor sit amet, consectetuer adipiscing elit, sed diam nonummy nibh euismod tincidunt ut laoreet dolore magna aliquam erat volutpat. Ut wisi enim ad minim veniam, quis nostrud exerci tation ullamcorper suscipit lobortis nisl ut aliquip ex ea commodo consequat. Duis autem vel eum iriure dolor in hendrerit in vulputate velit esse molestie consequat, vel illum dolore eu feugiat nulla facilisis. Lorem ipsum dolor sit amet, cons ectetuer adipiscing elit, sed diam nonummy nibh euismod tincidunt ut laoreet dolore magna aliquam erat volutpat.<br><br>Lorem ipsum dolor sit amet, consectetuer adipiscing elit, sed diam nonummy nibh euismod tincidunt ut laoreet dolore magna aliquam erat volutpat. Ut wisi enim ad minim veniam, quis nostrud exerci tation ullamcorper suscipit lobortis nisl ut aliquip ex ea commodo consequat.</div>
  <div class="t" style="left:161px;top:39px;font-size:8px">02. Text Added Here</div>
  <div class="p" style="left:161px;top:51px;width:121px">Lorem ipsum dolor sit amet, consectetuer adipiscing elit, sed diam nonummy nibh euismod tincidunt ut laoreet dolore magna aliquam erat volutpat. Ut wisi enim ad minim veniam, quis nostrud exerci tation ullamcorper suscipit lobortis nisl ut aliquip ex ea commodo consequat. Duis autem vel eum iriure dolor in hendrerit in vulputate velit esse molestie consequat, vel illum dolore eu feugiat nulla facilisis. Lorem ipsum dolor sit amet, cons ectetuer adipiscing elit, sed diam nonummy nibh euismod tincidunt ut laoreet dolore magna aliquam erat volutpat.<br><br>Lorem ipsum dolor sit amet, consectetuer adipiscing elit, sed diam nonummy nibh euismod tincidunt ut laoreet dolore magna aliquam erat volutpat. Ut wisi enim ad minim veniam, quis nostrud exerci tation ullamcorper suscipit lobortis nisl ut aliquip ex ea commodo consequat.</div>
  <div class="footer"><i></i><span>Marigold’s Lantern Foundation</span><em>9</em></div>
</section>

<!-- 10 Three columns -->
<section class="slide c1 r4">
  <div class="heading"><b>Heading</b> Goes Here</div>
  <div class="brand-mini"><i></i>Marigold’s Lantern</div>
  <div class="t" style="left:21px;top:38px;font-size:7px">01. Text Added Here</div>
  <div class="p" style="left:21px;top:48px;width:82px">Lorem ipsum dolor sit amet, consectetuer adipiscing elit, sed diam nonummy nibh euismod tincidunt ut laoreet dolore magna aliquam erat volutpat. Ut wisi enim ad minim veniam, quis nostrud exerci tation ullamcorper suscipit lobortis nisl ut aliquip ex ea commodo consequat. Duis autem vel eum iriure dolor in hendrerit in vulputate velit esse molestie consequat, vel illum dolore eu feugiat nulla facilisis.<br>Lorem ipsum dolor sit amet, consectetuer adipiscing elit, sed diam nonummy nibh euismod tincidunt ut laoreet dolore magna aliquam erat volutpat. Ut wisi enim ad minim veniam, quis nostrud exerci tation ullamcorper suscipit lobortis nisl ut aliquip ex ea commodo.<br>Lorem ipsum dolor sit amet, consectetuer adipiscing elit, sed diam nonummy nibh euismod tincidunt ut laoreet dolore.</div>
  <div class="t" style="left:112px;top:38px;font-size:7px">02. Text Added Here</div>
  <div class="p" style="left:112px;top:48px;width:82px">Lorem ipsum dolor sit amet, consectetuer adipiscing elit, sed diam nonummy nibh euismod tincidunt ut laoreet dolore magna aliquam erat volutpat. Ut wisi enim ad minim veniam, quis nostrud exerci tation ullamcorper suscipit lobortis nisl ut aliquip ex ea commodo consequat. Duis autem vel eum iriure dolor in hendrerit in vulputate velit esse molestie consequat, vel illum dolore eu feugiat nulla facilisis.<br>Lorem ipsum dolor sit amet, consectetuer adipiscing elit, sed diam nonummy nibh euismod tincidunt ut laoreet dolore magna aliquam erat volutpat. Ut wisi enim ad minim veniam, quis nostrud exerci tation ullamcorper suscipit lobortis nisl ut aliquip ex ea commodo.<br>Lorem ipsum dolor sit amet, consectetuer adipiscing elit, sed diam nonummy nibh euismod tincidunt ut laoreet dolore.</div>
  <div class="t" style="left:203px;top:38px;font-size:7px">03. Text Added Here</div>
  <div class="p" style="left:203px;top:48px;width:82px">Lorem ipsum dolor sit amet, consectetuer adipiscing elit, sed diam nonummy nibh euismod tincidunt ut laoreet dolore magna aliquam erat volutpat. Ut wisi enim ad minim veniam, quis nostrud exerci tation ullamcorper suscipit lobortis nisl ut aliquip ex ea commodo consequat. Duis autem vel eum iriure dolor in hendrerit in vulputate velit esse molestie consequat, vel illum dolore eu feugiat nulla facilisis.<br>Lorem ipsum dolor sit amet, consectetuer adipiscing elit, sed diam nonummy nibh euismod tincidunt ut laoreet dolore magna aliquam erat volutpat. Ut wisi enim ad minim veniam, quis nostrud exerci tation ullamcorper suscipit lobortis nisl ut aliquip ex ea commodo.<br>Lorem ipsum dolor sit amet, consectetuer adipiscing elit, sed diam nonummy nibh euismod tincidunt ut laoreet dolore.</div>
  <div class="footer"><i></i><span>Marigold’s Lantern Foundation</span><em>10</em></div>
</section>

<!-- 11 Puzzle cycle -->
<section class="slide c2 r4">
  <div class="heading"><b>Heading</b> Goes Here</div>
  <div class="brand-mini"><i></i>Marigold’s Lantern</div>
  <svg class="abs" style="left:108px;top:48px" width="90" height="90" viewBox="0 0 90 90">
    <path d="M43 2A43 43 0 0 0 2 43h20A23 23 0 0 1 43 22z" fill="#9a76ab"/>
    <path d="M47 2A43 43 0 0 1 88 43H68A23 23 0 0 0 47 22z" fill="#7d9fa8"/>
    <path d="M2 47A43 43 0 0 0 43 88V68A23 23 0 0 1 22 47z" fill="#7f8a7a"/>
    <path d="M88 47A43 43 0 0 1 47 88V68A23 23 0 0 0 68 47z" fill="#c79c9f"/>
    <circle cx="45" cy="14" r="4" fill="#fff"/><circle cx="76" cy="45" r="4" fill="#fff"/><circle cx="14" cy="45" r="4" fill="#fff"/><circle cx="45" cy="76" r="4" fill="#fff"/>
    <g fill="none" stroke="#fff" stroke-width="1.3"><circle cx="22" cy="22" r="4"/><circle cx="22" cy="22" r="1.5"/><path d="M65 25l6-6M63 22l4 4"/><rect x="18" y="63" width="8" height="6"/><circle cx="67" cy="67" r="4"/></g>
    <text x="45" y="43" text-anchor="middle" font-family="Poppins,sans-serif" font-size="7" font-weight="600" fill="#888">Text</text>
    <text x="45" y="52" text-anchor="middle" font-family="Poppins,sans-serif" font-size="7" font-weight="600" fill="#888">Added</text>
  </svg>
  <div class="t" style="left:71px;top:48px;font-size:5.5px;color:var(--blush);font-weight:600">Text Here</div>
  <div class="p" style="left:22px;top:55px;width:79px;text-align:right">Lorem ipsum dolor sit amet, consectetuer adipiscing elit, sed diammy nibh euismod tincidunt ut laoreet dolore</div>
  <div class="t" style="left:205px;top:48px;font-size:5.5px;color:var(--blush);font-weight:600">Text Here</div>
  <div class="p" style="left:205px;top:55px;width:79px;text-align:left">Lorem ipsum dolor sit amet, consectetuer adipiscing elit, sed diammy nibh euismod tincidunt ut laoreet dolore</div>
  <div class="t" style="left:71px;top:110px;font-size:5.5px;color:var(--blush);font-weight:600">Text Here</div>
  <div class="p" style="left:22px;top:117px;width:79px;text-align:right">Lorem ipsum dolor sit amet, consectetuer adipiscing elit, sed diammy nibh euismod tincidunt ut laoreet dolore</div>
  <div class="t" style="left:205px;top:110px;font-size:5.5px;color:var(--blush);font-weight:600">Text Here</div>
  <div class="p" style="left:205px;top:117px;width:79px;text-align:left">Lorem ipsum dolor sit amet, consectetuer adipiscing elit, sed diammy nibh euismod tincidunt ut laoreet dolore</div>
  <div class="footer"><i></i><span>Marigold’s Lantern Foundation</span><em>11</em></div>
</section>

<!-- 12 Four quadrant -->
<section class="slide c3 r4">
  <div class="heading"><b>Heading</b> Goes Here</div>
  <div class="brand-mini"><i></i>Marigold’s Lantern</div>
  <div class="grid-cell" style="left:103px;top:43px;background:var(--mauve);border-radius:6px 2px 2px 2px"><svg width="8" height="8" viewBox="0 0 24 24" fill="none" stroke="#fff" stroke-width="2"><circle cx="12" cy="12" r="5"/><path d="M12 2v4M12 18v4M2 12h4M18 12h4"/></svg><b>PROBLEM</b><p>Lorem ipsum dolor sit amet, cons ectetuer adipiscing elit, sed diam nonummy.</p></div>
  <div class="grid-cell" style="left:154px;top:43px;background:var(--teal);border-radius:2px 6px 2px 2px"><svg width="8" height="8" viewBox="0 0 24 24" fill="none" stroke="#fff" stroke-width="2"><path d="M12 3a6 6 0 0 0-3 11v3h6v-3a6 6 0 0 0-3-11zM10 21h4"/></svg><b>SOLUTION</b><p>Lorem ipsum dolor sit amet, cons ectetuer adipiscing elit, sed diam nonummy.</p></div>
  <div class="grid-cell" style="left:103px;top:92px;background:var(--sage);border-radius:2px 2px 2px 6px"><svg width="8" height="8" viewBox="0 0 24 24" fill="none" stroke="#fff" stroke-width="2"><path d="M3 21h18M6 17v-5M11 17V8M16 17v-7"/></svg><b>MARKET</b><p>Lorem ipsum dolor sit amet, cons ectetuer adipiscing elit, sed diam nonummy.</p></div>
  <div class="grid-cell" style="left:154px;top:92px;background:var(--blush);border-radius:2px 2px 6px 2px"><svg width="8" height="8" viewBox="0 0 24 24" fill="none" stroke="#fff" stroke-width="2"><circle cx="12" cy="12" r="8"/><circle cx="12" cy="12" r="4"/></svg><b>MISSION</b><p>Lorem ipsum dolor sit amet, cons ectetuer adipiscing elit, sed diam nonummy.</p></div>
  <div class="t" style="left:21px;top:51px;font-size:5.2px">01. Project Problem</div>
  <div class="p" style="left:21px;top:58px;width:72px;font-size:2.6px;line-height:3.4px">Lorem ipsum dolor sit amet, cons ectetuer adipiscing elit, sed diam nonummy euismod tincidunt Lorem ipsum dolor sit amet.</div>
  <div class="t" style="left:21px;top:100px;font-size:5.2px">03. Project Market</div>
  <div class="p" style="left:21px;top:107px;width:72px;font-size:2.6px;line-height:3.4px">Lorem ipsum dolor sit amet, cons ectetuer adipiscing elit, sed diam nonummy euismod tincidunt Lorem ipsum dolor sit amet.</div>
  <div class="t" style="left:215px;top:51px;font-size:5.2px">02. Project Solution</div>
  <div class="p" style="left:215px;top:58px;width:72px;font-size:2.6px;line-height:3.4px">Lorem ipsum dolor sit amet, cons ectetuer adipiscing elit, sed diam nonummy euismod tincidunt Lorem ipsum dolor sit amet.</div>
  <div class="t" style="left:215px;top:100px;font-size:5.2px">04. Project Mission</div>
  <div class="p" style="left:215px;top:107px;width:72px;font-size:2.6px;line-height:3.4px">Lorem ipsum dolor sit amet, cons ectetuer adipiscing elit, sed diam nonummy euismod tincidunt Lorem ipsum dolor sit amet.</div>
  <div class="footer"><i></i><span>Marigold’s Lantern Foundation</span><em>12</em></div>
</section>

<!-- 13 Three options -->
<section class="slide c1 r5">
  <div class="heading"><b>Heading</b> Goes Here</div>
  <div class="brand-mini"><i></i>Marigold’s Lantern</div>
  <svg class="abs" style="left:21px;top:77px" width="34" height="36" viewBox="0 0 34 36"><path d="M0 0h16l18 18-18 18H0l18-18z" fill="#ececec"/></svg>
  <div class="abs" role="img" aria-label="Expectant mother holding her belly" style="left:73px;top:40px;width:56px;height:66px;background:linear-gradient(160deg,#f3f1ee,#d8cfc7)"></div>
  <div class="abs" style="left:73px;top:106px;width:56px;height:1.5px;background:var(--mauve)"></div>
  <div class="abs" role="img" aria-label="Pregnant mother sharing a moment with her daughter" style="left:146px;top:40px;width:56px;height:66px;background:linear-gradient(160deg,#d9e4ea,#c7b39b)"></div>
  <div class="abs" style="left:146px;top:106px;width:56px;height:1.5px;background:var(--teal)"></div>
  <div class="abs" role="img" aria-label="Black and white portrait of a pregnant woman" style="left:219px;top:40px;width:56px;height:66px;background:linear-gradient(160deg,#eaeaea,#5c5c5c)"></div>
  <div class="abs" style="left:219px;top:106px;width:56px;height:1.5px;background:var(--blush)"></div>
  <div class="abs" style="left:73px;top:110px;font-size:5.5px;color:var(--mauve)">First <b style="color:#333">Option</b></div>
  <div class="p" style="left:73px;top:118px;width:44px;font-size:2.5px;line-height:3.2px;text-align:left">Lorem ipsum dolor sit consectetuer adipiscing elit, sed diam nonummy nibh euismod tincidunt ut dolore magna aliquam erat volutpat. Ut wisi enim ad minim veniam, quis nostrud</div>
  <div class="abs" style="left:146px;top:110px;font-size:5.5px;color:var(--teal)">Second <b style="color:#333">Option</b></div>
  <div class="p" style="left:146px;top:118px;width:44px;font-size:2.5px;line-height:3.2px;text-align:left">Lorem ipsum dolor sit consectetuer adipiscing elit, sed diam nonummy nibh euismod tincidunt ut dolore magna aliquam erat volutpat. Ut wisi enim ad minim veniam, quis nostrud</div>
  <div class="abs" style="left:219px;top:110px;font-size:5.5px;color:var(--blush)">Third <b style="color:#333">Option</b></div>
  <div class="p" style="left:219px;top:118px;width:44px;font-size:2.5px;line-height:3.2px;text-align:left">Lorem ipsum dolor sit consectetuer adipiscing elit, sed diam nonummy nibh euismod tincidunt ut dolore magna aliquam erat volutpat. Ut wisi enim ad minim veniam, quis nostrud</div>
  <div class="footer"><i></i><span>Marigold’s Lantern Foundation</span><em>13</em></div>
</section>

<!-- 14 Six features -->
<section class="slide c2 r5">
  <div class="heading"><b>Heading</b> Goes Here</div>
  <div class="brand-mini"><i></i>Marigold’s Lantern</div>
  <div class="feat-box" style="left:57px;top:38px;color:var(--mauve)"><svg width="13" height="11" viewBox="0 0 24 20" fill="none" stroke="#fff" stroke-width="1.6"><circle cx="8" cy="6" r="3"/><circle cx="16" cy="6" r="3"/><path d="M2 18c0-4 3-6 6-6s6 2 6 6M10 18c0-4 3-6 6-6s6 2 6 6"/></svg></div>
  <div class="feat-box" style="left:141px;top:38px;color:var(--teal)"><svg width="12" height="12" viewBox="0 0 24 24" fill="none" stroke="#fff" stroke-width="1.6"><circle cx="12" cy="12" r="9"/><circle cx="9" cy="10" r="2"/><path d="M13 14h5"/></svg></div>
  <div class="feat-box" style="left:226px;top:38px;color:var(--blush)"><svg width="12" height="12" viewBox="0 0 24 24" fill="none" stroke="#fff" stroke-width="1.6"><path d="M3 21h18M6 17v-4M11 17V9M16 17V5"/></svg></div>
  <div class="feat-title" style="left:34px;top:66px">LOREM IPSUM</div>
  <div class="feat-title" style="left:118px;top:66px">LOREM IPSUM</div>
  <div class="feat-title" style="left:203px;top:66px">LOREM IPSUM</div>
  <div class="p center" style="left:44px;top:72px;width:50px;font-size:2.4px;line-height:3px">Lorem ipsum dolor sit amet, consectetuer adipiscing elit, sed diam nonummy nibh euismod tincidunt ut laoreet</div>
  <div class="p center" style="left:128px;top:72px;width:50px;font-size:2.4px;line-height:3px">Lorem ipsum dolor sit amet, consectetuer adipiscing elit, sed diam nonummy nibh euismod tincidunt ut laoreet</div>
  <div class="p center" style="left:213px;top:72px;width:50px;font-size:2.4px;line-height:3px">Lorem ipsum dolor sit amet, consectetuer adipiscing elit, sed diam nonummy nibh euismod tincidunt ut laoreet</div>
  <div class="feat-box" style="left:57px;top:97px;color:var(--sage)"><svg width="12" height="12" viewBox="0 0 24 24" fill="none" stroke="#fff" stroke-width="1.6"><path d="M3 3v18h18M6 8l6 6 3-3 5 5"/></svg></div>
  <div class="feat-box" style="left:141px;top:97px;color:var(--blush)"><svg width="12" height="12" viewBox="0 0 24 24" fill="none" stroke="#fff" stroke-width="1.6"><path d="M9 3h6l-2 4h-2zM6 21h12a6 6 0 0 0-6-14 6 6 0 0 0-6 14z"/></svg></div>
  <div class="feat-box" style="left:226px;top:97px;color:var(--mauve)"><svg width="12" height="12" viewBox="0 0 24 24" fill="none" stroke="#fff" stroke-width="1.6"><circle cx="12" cy="10" r="6"/><path d="M9 15l-2 7 5-3 5 3-2-7"/></svg></div>
  <div class="feat-title" style="left:34px;top:125px">LOREM IPSUM</div>
  <div class="feat-title" style="left:118px;top:125px">LOREM IPSUM</div>
  <div class="feat-title" style="left:203px;top:125px">LOREM IPSUM</div>
  <div class="p center" style="left:44px;top:131px;width:50px;font-size:2.4px;line-height:3px">Lorem ipsum dolor sit amet, consectetuer adipiscing elit, sed diam nonummy nibh euismod tincidunt ut laoreet</div>
  <div class="p center" style="left:128px;top:131px;width:50px;font-size:2.4px;line-height:3px">Lorem ipsum dolor sit amet, consectetuer adipiscing elit, sed diam nonummy nibh euismod tincidunt ut laoreet</div>
  <div class="p center" style="left:213px;top:131px;width:50px;font-size:2.4px;line-height:3px">Lorem ipsum dolor sit amet, consectetuer adipiscing elit, sed diam nonummy nibh euismod tincidunt ut laoreet</div>
  <div class="footer"><i></i><span>Marigold’s Lantern Foundation</span><em>14</em></div>
</section>

<!-- 15 Numbered list -->
<section class="slide c3 r5">
  <div class="heading"><b>Heading</b> Goes Here</div>
  <div class="brand-mini"><i></i>Marigold’s Lantern</div>
  <div class="photo" role="img" aria-label="Open hands holding a green butterfly" style="left:27px;top:39px;width:106px;height:105px;background:radial-gradient(circle at 50% 55%,#2f7a6b 0 12%,#e8c2a5 34%,#f5ece6 75%)"></div>
  <div class="num-sq" style="top:49px">1.</div>
  <div class="t" style="left:170px;top:48px;font-size:7px">Lorem Ipsum</div>
  <div class="p" style="left:170px;top:57px;width:110px;font-size:3.3px;text-align:left">Lorem ipsum dolor sit amet, consectetuer adipiscing elit, sed diam nonummy nibh euismod tincid</div>
  <div class="num-sq" style="top:83px">2.</div>
  <div class="t" style="left:170px;top:82px;font-size:7px">Lorem Ipsum</div>
  <div class="p" style="left:170px;top:91px;width:110px;font-size:3.3px;text-align:left">Lorem ipsum dolor sit amet, consectetuer adipiscing elit, sed diam nonummy nibh euismod tincid</div>
  <div class="num-sq" style="top:117px">3.</div>
  <div class="t" style="left:170px;top:116px;font-size:7px">Lorem Ipsum</div>
  <div class="p" style="left:170px;top:125px;width:110px;font-size:3.3px;text-align:left">Lorem ipsum dolor sit amet, consectetuer adipiscing elit, sed diam nonummy nibh euismod tincid</div>
  <div class="footer"><i></i><span>Marigold’s Lantern Foundation</span><em>15</em></div>
</section>

<!-- 16 Timeline -->
<section class="slide c1 r6">
  <div class="heading"><b>Heading</b> Goes Here</div>
  <div class="brand-mini"><i></i>Marigold’s Lantern</div>
  <div class="tl-item" style="left:24px;top:44px"><b>YOUR TITLE</b><span>Refers to a good or service being offered</span></div>
  <div class="tl-item" style="left:123px;top:44px"><b>YOUR TITLE</b><span>Refers to a good or service being offered</span></div>
  <div class="tl-item" style="left:223px;top:44px"><b>YOUR TITLE</b><span>Refers to a good or service being offered</span></div>
  <svg class="abs" style="left:0;top:0" width="305" height="172" viewBox="0 0 305 172">
    <g stroke="#7d9fa8" stroke-width="1"><path d="M54 68v14M153 68v14M253 68v14M104 97v12M203 97v12"/></g>
    <g fill="#7d9fa8"><circle cx="54" cy="70" r="1.6"/><circle cx="153" cy="70" r="1.6"/><circle cx="253" cy="70" r="1.6"/></g>
    <g fill="#7f8a7a"><circle cx="104" cy="107" r="1.6"/><circle cx="203" cy="107" r="1.6"/></g>
    <path d="M34 86h42l-6 8H28z" fill="#9a76ab"/>
    <path d="M78 86h50l-6 8H72z" fill="#7d9fa8" transform="translate(0,0)"/>
    <path d="M130 86h46l6 8h-46z" fill="#9a76ab"/>
    <path d="M178 86h46l-6 8h-46z" fill="#7d9fa8"/>
    <path d="M226 86h44l6 8h-44z" fill="#9a76ab"/>
    <g font-family="Poppins,sans-serif" font-size="4.4" font-weight="600" fill="#fff" text-anchor="middle"><text x="53" y="92">1990</text><text x="102" y="92">2001</text><text x="153" y="92">2007</text><text x="203" y="92">2012</text><text x="253" y="92">2020</text></g>
  </svg>
  <div class="tl-item" style="left:74px;top:118px"><b>YOUR TITLE</b><span>Refers to a good or service being offered</span></div>
  <div class="tl-item" style="left:173px;top:118px"><b>YOUR TITLE</b><span>Refers to a good or service being offered</span></div>
  <div class="footer"><i></i><span>Marigold’s Lantern Foundation</span><em>16</em></div>
</section>

<!-- 17 Team -->
<section class="slide c2 r6">
  <div class="heading"><b>Heading</b> Goes Here</div>
  <div class="brand-mini"><i></i>Marigold’s Lantern</div>
  <div class="team" style="left:28px"><div class="band" style="background:var(--mauve)"></div><div class="avatar" role="img" aria-label="Team member portrait" style="background:#d8d3d6"></div><b style="color:var(--mauve)">OWEN HALE</b><p>Ipsum dolor sit amet, cons ectetuer adipiscing elit, sed diam nonummy nibh euismod tincidunt ut laoreet dolore magna.</p></div>
  <div class="team" style="left:97px"><div class="band" style="background:var(--teal)"></div><div class="avatar" role="img" aria-label="Team member portrait" style="background:#d4d9db"></div><b style="color:var(--teal)">ROSA LIND</b><p>Ipsum dolor sit amet, cons ectetuer adipiscing elit, sed diam nonummy nibh euismod tincidunt ut laoreet dolore magna.</p></div>
  <div class="team" style="left:166px"><div class="band" style="background:var(--mauve)"></div><div class="avatar" role="img" aria-label="Team member portrait" style="background:#d8d3d6"></div><b style="color:var(--mauve)">OWEN HALE</b><p>Ipsum dolor sit amet, cons ectetuer adipiscing elit, sed diam nonummy nibh euismod tincidunt ut laoreet dolore magna.</p></div>
  <div class="team" style="left:235px"><div class="band" style="background:var(--teal)"></div><div class="avatar" role="img" aria-label="Team member portrait" style="background:#d4d9db"></div><b style="color:var(--teal)">ROSA LIND</b><p>Ipsum dolor sit amet, cons ectetuer adipiscing elit, sed diam nonummy nibh euismod tincidunt ut laoreet dolore magna.</p></div>
  <div class="footer"><i></i><span>Marigold’s Lantern Foundation</span><em>17</em></div>
</section>

<!-- 18 Thank you -->
<section class="slide c3 r6" style="background:linear-gradient(180deg,#b48fc4 0%,#a884bb 55%,#c39bc2 100%)">
  <div class="abs" style="left:22px;top:28px;font-size:10px;line-height:12px;font-weight:500;color:#fff">Marigold’s Lantern<br><span style="font-size:5px;line-height:7px">Pregnancy &amp; Family Support</span></div>
  <div class="abs" style="left:25px;top:80px;font-size:18px;font-weight:700;color:#fff">Thank You</div>
  <div class="contact" style="top:105px"><svg width="7" height="7" viewBox="0 0 24 24" fill="#fff"><path d="M6 2l4 4-2 3a12 12 0 0 0 7 7l3-2 4 4-3 4C10 21 3 14 2 5z"/></svg><span class="bar"></span><span>+1 555 0142 7730<br>+1 555 0142 7731</span></div>
  <div class="contact" style="top:124px"><svg width="7" height="7" viewBox="0 0 24 24" fill="#fff"><path d="M2 11L22 3l-8 19-3-8z"/></svg><span class="bar"></span><span>www.websitename.com<br>urname@email.com</span></div>
  <div class="contact" style="top:143px"><svg width="7" height="7" viewBox="0 0 24 24" fill="#fff"><path d="M12 3l10 9h-3v9h-5v-6h-4v6H5v-9H2z"/></svg><span class="bar"></span><span>1234 Street name, town/city,<br>state/country, post/zip 012345.</span></div>
</section>

</div>
</body>
</html>
```